BRIGHTDESK - Remote Tech Support Site

We are looking for a new very responsive and simple website for our brand Brightdesk.com - a remote technical support company.

This company supports customers Globally in different countries throughout Eur/ North America / South America / Asia etc (please keep this in mind and integrate into the idea).

Its important to us that the design is very explanatory, the customer should easily be able to figure out that we provide computer support right away ... I like one page responsive type designs as well without a bunch of menu items

Here are some similar sites we like - but still looking for a unique design that fits out brand "brightdesk" - I have upload also some layouts i like (but the designs are not important just the layouts), youll see it includes consumer business etc which is important.

VOLM.COM - I love how clean it is - nice and white easy to see everything

PLUMWIRE247.COM - also nice the layout and responsive one page design makes it easy to use

corvalfix.com - similar to plumwire design as well - you can get the idea im looking for between the two

You will notice those examples are much different then the attachments I added - again this is more of an idea for possible layouts .. attached is also the logo - could inspire color scheme / blue white black etc

Target Market(s)

Home consumers without computer knowledge , older age 45-65, small medium business ... computer repair - slow computers

Industry/Entity Type

Computer Repair

Logo Text

Brightdesk

Coding

Coded - Design and coding required

Number of Pages Required

1 page

Font styles to use
Sans Serif
Other font styles liked:
• your choice responsive

Colors

Designer to choose colors to be used in the design.

Requirements
Must have
• Clean - responsive - professional design - the name says it all - brightdesk
• CALL TO ACTIONS FOR "Get Help Now!" / "Learn More" etc
Nice to have
• We are looking for a new very responsive and simple website for our brand Brightdesk.com - a remote technical support company.
• This company supports customers Globally in different countries throughout Eur/ North America / South America / Asia etc (please keep this in mind and integrate into the idea).
• Its important to us that the design is very explanatory, the customer should easily be able to figure out that we provide computer support right away ... I like one page responsive type designs as well without a bunch of menu items
• Here are some similar sites we like - but still looking for a unique design that fits out brand "brightdesk" - I have upload also some layouts i like (but the designs are not important just the layouts), youll see it includes consumer business etc which is important.
• VOLM.COM - I love how clean it is - nice and white easy to see everything
• PLUMWIRE247.COM - also nice the layout and responsive one page design makes it easy to use
• corvalfix.com - similar to plumwire design as well - you can get the idea im looking for between the two
Should not have
• dark, packed page - bad small font -

```html
<!DOCTYPE html>
<html lang="en">
<head>
<meta charset="utf-8">
<title>Brightdesk – Remote Tech Support</title>
<link href="https://fonts.googleapis.com/css2?family=Montserrat:wght@400;500;600;700;800&family=Open+Sans:wght@400;600&display=swap" rel="stylesheet">
<style>
:root{
  --blue:#1e8ff0;
  --blue-dark:#1473c9;
  --green:#7dc41f;
  --green-dark:#66a814;
  --ink:#222;
  --muted:#666;
  --black:#0b0b0b;
  --pale:#f3fafd;
  --white:#fff;
}
*{box-sizing:border-box;margin:0;padding:0}
html,body{width:1200px;height:3727px;overflow:hidden}
body{background:var(--white);font-family:"Open Sans",Arial,sans-serif;color:var(--ink);position:relative}
h1,h2,h3,h4,.mont{font-family:"Montserrat",Arial,sans-serif}
.abs{position:absolute}
.btn{display:inline-block;background:var(--blue);color:#fff;font-family:"Montserrat",sans-serif;font-weight:600;text-align:center;text-decoration:none;border-radius:2px}

/* top bar & nav */
.topbar{top:0;left:0;width:1200px;height:25px;background:var(--black);color:#fff;font-size:11px}
.topbar .social{position:absolute;left:246px;top:6px;display:flex;gap:9px}
.topbar .social span{width:12px;height:12px;border-radius:50%;border:1.5px solid #fff;display:block}
.topbar .right{position:absolute;right:250px;top:5px;display:flex;gap:22px}
.nav{top:25px;left:0;width:1200px;height:45px;background:#fff;border-bottom:1px solid #eee}
.logo{position:absolute;left:248px;top:10px;display:flex;align-items:center;gap:6px;font-family:"Montserrat",sans-serif;font-weight:600;font-size:17px;color:var(--blue)}
.logo i{width:22px;height:22px;border-radius:50%;background:var(--blue);display:block}
.menu{position:absolute;left:482px;top:12px;display:flex;gap:4px;font-family:"Montserrat",sans-serif;font-size:12px}
.menu a{padding:4px 9px;color:var(--ink);text-decoration:none}
.menu a.on{background:var(--blue);color:#fff}
.contact-mini{position:absolute;left:815px;top:10px;font-size:11px;line-height:14px}
.contact-mini b{color:var(--blue);font-weight:400}

/* hero */
.hero{top:70px;left:0;width:1200px;height:402px;overflow:hidden}
.hero .photo-left{position:absolute;inset:0;background:linear-gradient(90deg,#3b3d3f 0%,#7b7a76 40%,#c9c6bd 100%)}
.hero .photo-right{position:absolute;top:0;right:0;height:402px;width:680px;background:linear-gradient(120deg,#e8eef3 0%,#b9c6cf 55%,#9aa9b3 100%);clip-path:polygon(92px 0,100% 0,100% 100%,0 100%)}
.hero-copy{position:absolute;left:248px;top:42px;color:#fff}
.hero-copy h1{font-size:29px;font-weight:700;line-height:33px}
.hero-list{margin-top:18px;display:grid;grid-template-columns:145px 170px;row-gap:12px;font-size:11px;font-family:"Montserrat",sans-serif}
.hero-list li{list-style:none;padding-left:12px;position:relative}
.hero-list li:before{content:"";position:absolute;left:0;top:3px;width:6px;height:6px;background:var(--green);border-radius:50%}
.member-box{position:absolute;left:286px;top:233px;width:216px;height:82px;border:2px dashed rgba(255,255,255,.8);color:#fff;text-align:center;font-family:"Montserrat",sans-serif}
.member-box h3{font-size:18px;font-weight:500;margin-top:8px;letter-spacing:.5px}
.member-box .price{font-size:34px;font-weight:700;line-height:34px;color:#fff}
.member-box .price small{font-size:10px;font-weight:400}
.member-box .sub{font-size:9px}
.hero .cta{position:absolute;left:328px;top:322px;width:132px;height:28px;line-height:28px;font-size:13px}
.dots{position:absolute;left:908px;top:368px;display:flex;gap:3px}
.dots span{width:14px;height:14px;background:#fff;display:block;opacity:.7}
.dots span.on{background:var(--blue);opacity:1}

/* about */
.about{top:472px;left:0;width:1200px;height:166px}
.about h2{position:absolute;left:248px;top:46px;color:var(--green);font-size:28px;font-weight:800;line-height:29px}
.about p{position:absolute;left:455px;width:495px;font-size:11px;line-height:17px;color:var(--muted)}

/* stats */
.stats{top:638px;left:248px;width:702px;height:90px;background:var(--blue);color:#fff;display:flex;justify-content:space-around;align-items:center;padding:0 20px}
.stats:before,.stats:after{content:"";position:absolute;left:0;right:0;height:6px;background:radial-gradient(circle at 5px 0,#fff 3px,transparent 3.5px) repeat-x;background-size:10px 6px}
.stats:before{top:0}
.stats:after{bottom:0;transform:rotate(180deg)}
.stat{display:flex;flex-direction:column;align-items:flex-start;font-family:"Montserrat",sans-serif;font-size:12px;font-weight:700;line-height:15px}
.stat svg{margin-bottom:4px}

/* support */
.support{top:728px;left:0;width:1200px;height:457px;background:#eceeef;overflow:hidden}
.support .photo{position:absolute;left:0;top:0;width:640px;height:457px;background:linear-gradient(100deg,#d9dcdf 0%,#c7b8a9 45%,#e5e7e9 100%)}
.support svg.ring{position:absolute;left:60px;top:-40px}
.support-copy{position:absolute;left:666px;top:50px}
.support-copy h2{color:var(--blue);font-size:29px;font-weight:700;line-height:32px}
.ticks{margin-top:18px;font-size:12px;font-family:"Montserrat",sans-serif;line-height:23px}
.ticks li{list-style:none;padding-left:16px;position:relative}
.ticks li:before{content:"";position:absolute;left:0;top:8px;border-left:8px solid var(--green);border-top:4px solid transparent;border-bottom:4px solid transparent}
.support-copy .from{margin-top:14px;font-size:12px;font-family:"Montserrat",sans-serif}
.support-copy .big{font-family:"Montserrat",sans-serif;color:var(--green);font-size:48px;font-weight:700;line-height:48px}
.support-copy .big small{font-size:14px;font-weight:500}
.support-copy .btn{margin-top:18px;width:186px;height:42px;line-height:42px;font-size:15px}

/* features */
.features{top:1185px;left:0;width:1200px;height:728px;background:var(--pale);overflow:hidden}
.features h2{position:absolute;top:28px;width:100%;text-align:center;color:var(--blue);font-size:29px;font-weight:700;line-height:36px}
.feat{position:absolute;width:170px;text-align:center;z-index:2}
.feat .ic{width:60px;height:60px;border:2px solid var(--blue);border-radius:50%;margin:0 auto 8px;display:flex;align-items:center;justify-content:center;background:#fff}
.feat h4{font-size:12px;font-weight:600;letter-spacing:.3px;white-space:nowrap}
.feat p{font-size:10px;color:var(--muted);line-height:13px;margin-top:3px}
.features .photo{position:absolute;left:790px;top:207px;width:410px;height:398px;z-index:1;background:linear-gradient(90deg,rgba(243,250,253,0) 0%,#d6ccc1 22%,#c3b6a8 60%,#b9aa9b 100%)}
.callbar{position:absolute;left:467px;top:636px;width:266px;height:55px;background:var(--green);color:#fff;display:flex;align-items:center;gap:10px;padding-left:24px;font-family:"Montserrat",sans-serif}
.callbar small{display:block;font-size:10px;font-weight:600}
.callbar b{font-size:22px;font-weight:600}

/* pricing */
.pricing{top:1913px;left:0;width:1200px;height:373px;background:linear-gradient(90deg,#2b2623 0%,#4a423d 50%,#2e2a27 100%)}
.pricing h2{position:absolute;top:38px;width:100%;text-align:center;color:#fff;font-size:29px;font-weight:600}
.plan{position:absolute;top:105px;width:196px;height:219px;background:#fff;text-align:center}
.plan h3{height:34px;line-height:34px;color:var(--green-dark);font-size:16px;font-weight:700}
.plan .band{background:var(--green);color:#fff;padding:6px 0 4px;font-family:"Montserrat",sans-serif}
.plan .band b{font-size:32px;font-weight:700;line-height:34px;display:block}
.plan .band small{font-size:8px}
.plan p{font-size:10px;line-height:14px;color:#555;padding:14px 12px 8px}
.plan .btn{width:124px;height:28px;line-height:28px;font-size:12px}

/* how */
.how{top:2286px;left:0;width:1200px;height:286px}
.how h2{position:absolute;top:36px;width:100%;text-align:center;color:var(--green);font-size:28px;font-weight:700}
.step{position:absolute;top:98px;width:240px;text-align:center}
.step h4{font-size:12px;font-weight:600;margin-top:6px}
.step p{font-size:10px;color:var(--muted);line-height:13px;margin-top:3px}
.how .btn{position:absolute;left:522px;top:216px;width:154px;height:33px;line-height:33px;font-size:12px}

/* testimonials */
.testi{top:2572px;left:0;width:1200px;height:211px;background:linear-gradient(90deg,#1a86e6,#2295f2 50%,#1a86e6)}
.testi h2{position:absolute;top:22px;width:100%;text-align:center;color:#fff;font-size:29px;font-weight:600}
.quote{position:absolute;top:88px;width:320px;color:#fff;font-size:10px;line-height:13px}
.quote .stars{color:#f9c513;font-size:10px;letter-spacing:1px}
.quote .who{margin-top:6px;opacity:.85}
.tdots{position:absolute;left:592px;top:183px;display:flex;gap:5px}
.tdots span{width:7px;height:7px;border-radius:50%;background:#fff;opacity:.5}
.tdots span.on{opacity:1}

/* call today */
.calltoday{top:2783px;left:0;width:1200px;height:385px;text-align:center}
.calltoday h2{margin-top:30px;color:var(--green);font-size:24px;font-weight:700;line-height:26px}
.calltoday h3{color:var(--blue);font-size:24px;font-weight:500;line-height:28px}
.video{position:absolute;left:368px;top:94px;width:464px;height:236px;background:linear-gradient(180deg,#d9d4c6 0%,#cfc7b4 70%,#b48c5d 100%)}
.video .play{position:absolute;left:210px;top:96px;width:44px;height:32px;background:#e62117;border-radius:8px}
.video .play:after{content:"";position:absolute;left:17px;top:9px;border-left:12px solid #fff;border-top:7px solid transparent;border-bottom:7px solid transparent}
.calltoday .cap{position:absolute;top:351px;width:100%;font-size:12px;font-weight:600}

/* footer */
.footer{top:3168px;left:0;width:1200px;height:348px;background:var(--black);color:#fff}
.footer .logo{left:248px;top:22px;color:#fff}
.footer .logo i{background:#fff}
.f-about{position:absolute;left:248px;top:58px;width:215px;font-size:10px;line-height:14px;color:#ddd}
.f-about p+p{margin-top:10px}
.f-h{position:absolute;font-family:"Montserrat",sans-serif;font-size:12px;font-weight:600}
.f-links{position:absolute;left:522px;top:62px;font-size:10px;line-height:17px;list-style:none;color:#ddd}
.badges{position:absolute;left:248px;top:240px;display:flex;gap:16px;align-items:center}
.badges span{display:block;background:#c9a227}
.follow{position:absolute;left:522px;top:240px;display:flex;gap:10px}
.follow span{width:28px;height:28px;border:2px solid #fff;border-radius:50%;display:block}
.copy{position:absolute;left:248px;top:326px;font-size:9px;color:#ccc}
.contact-panel{position:absolute;left:706px;top:0;width:246px;height:348px;background:var(--blue);padding:22px 14px}
.contact-panel h3{text-align:center;font-size:18px;font-weight:600}
.contact-panel .field{background:#fff;height:34px;margin-top:10px;font-size:8px;color:#999;padding:6px 8px}
.contact-panel .field.msg{height:120px}
.contact-panel .send{display:block;margin:16px auto 0;width:190px;height:34px;border:2px solid #fff;text-align:center;line-height:30px;font-family:"Montserrat",sans-serif;font-size:14px}
</style>
</head>
<body>

<div class="abs topbar">
  <div class="social"><span></span><span></span><span></span><span></span></div>
  <div class="right"><span>EN ▾</span><span>login</span></div>
</div>

<header class="abs nav">
  <div class="logo"><i></i>brightdesk</div>
  <nav class="menu"><a class="on" href="#">Home</a><a href="#">About Us</a><a href="#">Services</a><a href="#">Contact Us</a></nav>
  <div class="contact-mini"><b>☎</b> (888) 555-0142<br><b>✉</b> info@brightdesk.com</div>
</header>

<section class="abs hero">
  <div class="photo-left" role="img" aria-label="Smiling older woman in a bright room, softly faded"></div>
  <div class="photo-right" role="img" aria-label="Happy older man using a laptop at home"></div>
  <svg class="abs" style="left:0;top:0" width="1200" height="402"><path d="M612 0 L520 402" stroke="#7dc41f" stroke-width="7"/></svg>
  <div class="hero-copy">
    <h1>Dedicated Support<br>Anytime. Anywhere.</h1>
    <ul class="hero-list">
      <li>Instant Support</li><li>Quick Setup &amp; Install</li>
      <li>Real-Time Optimization</li><li>Leading Security Software</li>
      <li>Free Diagnostic</li><li>Unlimited Cloud Backup</li>
    </ul>
  </div>
  <div class="member-box">
    <h3>MEMBERSHIPS</h3>
    <div class="price">19.99<small>/month</small></div>
    <div class="sub">Starting at</div>
  </div>
  <a class="btn cta" href="#">Get it Now</a>
  <div class="dots"><span></span><span class="on"></span></div>
</section>

<section class="abs about">
  <h2>YOU HAVE<br>TO KNOW<br>ABOUT US</h2>
  <p style="top:46px">Our team is a leader in providing top notch quality services and products with a focus on our customer's needs. We are happy to discuss your computer issues and provide a free valuable diagnostic to determine the best solutions.</p>
  <p style="top:104px">Whether you are looking for the best source out there, we have everything for your computer and internet security!</p>
</section>

<section class="abs stats">
  <div class="stat"><svg width="22" height="18" viewBox="0 0 22 18" fill="#fff"><circle cx="7" cy="5" r="4"/><circle cx="16" cy="6" r="3"/><path d="M0 18c0-5 3-7 7-7s7 2 7 7zM13 18c0-3 1-5 3-5s6 1 6 5z"/></svg>25000 +<br>CUSTOMERS</div>
  <div class="stat"><svg width="22" height="18" viewBox="0 0 22 18" fill="none" stroke="#fff" stroke-width="2"><rect x="3" y="2" width="16" height="11"/><path d="M0 16h22"/></svg>175 +<br>EMPLOYEES</div>
  <div class="stat"><svg width="16" height="20" viewBox="0 0 16 20" fill="none" stroke="#fff" stroke-width="2"><rect x="2" y="1" width="12" height="18"/><path d="M5 5h6M5 9h6"/></svg>65000 +<br>COMPUTERS REPAIRED</div>
  <div class="stat"><svg width="20" height="18" viewBox="0 0 20 18" fill="#fff"><path d="M10 18L1 9a5 5 0 0 1 9-6 5 5 0 0 1 9 6z"/></svg>2 +<br>YEARS IN BUSINESS</div>
</section>

<section class="abs support">
  <div class="photo" role="img" aria-label="Friendly support technician wearing a headset"></div>
  <svg class="ring" width="600" height="560"><circle cx="288" cy="270" r="258" fill="none" stroke="#7dc41f" stroke-width="12"/></svg>
  <div class="support-copy">
    <h2>Real-Time Support<br>Features and<br>BENEFITS</h2>
    <ul class="ticks">
      <li>24/7 Real-Time Technician Support</li>
      <li>The best Security Software in the market</li>
      <li>Regular tune-ups and optimization</li>
      <li>Setup and installation included</li>
    </ul>
    <div class="from">Starting At Only</div>
    <div class="big">$19.99<small>/month</small></div>
    <a class="btn" href="#">Become a Member</a>
  </div>
</section>

<section class="abs features">
  <h2>ALL THE BEST FEATURES,<br>AT THE BEST PRICE!</h2>
  <div class="photo" role="img" aria-label="Older couple smiling together on a sofa"></div>
  <div class="feat" style="left:245px;top:160px"><div class="ic"><svg width="28" height="24" fill="none" stroke="#1e8ff0" stroke-width="2"><rect x="2" y="3" width="24" height="16"/><path d="M9 11h10"/></svg></div><h4>AD BLOCKER</h4><p>Avoid unwanted Pop-ups with the newest Ad Blocking technology</p></div>
  <div class="feat" style="left:425px;top:160px"><div class="ic"><svg width="28" height="24" fill="none" stroke="#1e8ff0" stroke-width="2"><rect x="2" y="3" width="24" height="16"/><path d="M6 15l5-5 4 3 6-6"/></svg></div><h4>REGULAR TUNE-UPS</h4><p>Get a Regular Tune-Up and Optimization every 90 days</p></div>
  <div class="feat" style="left:603px;top:160px"><div class="ic"><svg width="28" height="24" fill="none" stroke="#1e8ff0" stroke-width="2"><rect x="2" y="3" width="24" height="16"/><path d="M7 9h14M7 13h9"/></svg></div><h4>SYSTEM REPORTS</h4><p>Stay up to date with Real-Time System Reporting</p></div>
  <div class="feat" style="left:245px;top:330px"><div class="ic"><svg width="26" height="26" fill="none" stroke="#1e8ff0" stroke-width="2"><rect x="3" y="3" width="20" height="20"/><circle cx="13" cy="11" r="4"/><path d="M6 22c1-4 4-5 7-5s6 1 7 5"/></svg></div><h4>IDENTITY PROTECTION</h4><p>Coming Soon</p></div>
  <div class="feat" style="left:425px;top:330px"><div class="ic"><svg width="18" height="28" fill="none" stroke="#1e8ff0" stroke-width="2"><rect x="2" y="2" width="14" height="24" rx="2"/><path d="M7 22h4"/></svg></div><h4>MOBILE SECURITY</h4><p>Coming Soon</p></div>
  <div class="feat" style="left:603px;top:330px"><div class="ic"><svg width="28" height="26" fill="none" stroke="#1e8ff0" stroke-width="2"><rect x="2" y="3" width="18" height="13"/><rect x="18" y="10" width="8" height="14"/><path d="M7 21h8"/></svg></div><h4>CROSS PLATFORM SUPPORT</h4><p>One Support Plan for different<br>types of devices</p></div>
  <div class="feat" style="left:330px;top:478px"><div class="ic"><svg width="28" height="26" fill="none" stroke="#1e8ff0" stroke-width="2"><rect x="2" y="3" width="16" height="11"/><rect x="14" y="10" width="12" height="14"/></svg></div><h4>MULTIPLE DEVICES</h4><p>Get support for up to 4 multiple devices. Ask about our Family Plans</p></div>
  <div class="feat" style="left:516px;top:478px"><div class="ic"><svg width="30" height="22" fill="none" stroke="#1e8ff0" stroke-width="2"><path d="M8 19a6 6 0 0 1 0-12 8 8 0 0 1 15 2 5 5 0 0 1 0 10z"/><path d="M15 10v7M12 14l3 3 3-3"/></svg></div><h4>CLOUD BACKUP</h4><p>Keep your data safe! Ask about our plans for Unlimited Cloud Backup</p></div>
  <div class="callbar">
    <svg width="30" height="26" viewBox="0 0 30 26" fill="#fff"><path d="M2 8c0-4 26-4 26 0v3h-7V8H9v3H2z"/><rect x="6" y="12" width="18" height="12" rx="2"/><circle cx="15" cy="18" r="3" fill="#7dc41f"/></svg>
    <div><small>Call Us Today</small><b>(888) 555-0142</b></div>
  </div>
</section>

<section class="abs pricing" role="img" aria-label="Family using devices together, darkened background">
  <h2>MEMBERSHIP PRICING AND PLANS</h2>
  <div class="plan" style="left:281px"><h3>PREMIUM</h3><div class="band"><b>$19.99</b><small>(with $100 setup fee)</small></div><p>Regular 90 Day Optimization<br>Unlimited 24/7 Tier 3 Technician Support</p><a class="btn" href="#">Learn More</a></div>
  <div class="plan" style="left:504px"><h3>PREMIUM PLUS</h3><div class="band"><b>$29.99</b><small>(with $100 setup fee)</small></div><p>Regular 90 Day Optimization<br>Unlimited 24/7 Tier 3 Technician Support</p><a class="btn" href="#">Learn More</a></div>
  <div class="plan" style="left:728px"><h3>PLATINUM</h3><div class="band"><b>$39.99</b><small>(with $100 setup fee)</small></div><p>Regular 90 Day Optimization<br>Unlimited 24/7 Tier 3 Technician Support</p><a class="btn" href="#">Learn More</a></div>
</section>

<section class="abs how">
  <h2>HOW IT WORKS</h2>
  <div class="step" style="left:213px"><svg width="30" height="30" fill="none" stroke="#1e8ff0" stroke-width="2"><path d="M4 18v8h22v-8"/><path d="M15 3v15M9 12l6 6 6-6"/></svg><h4>FREE DIAGNOSTIC</h4><p>Get a diagnostic FOR FREE! Get a free consultation with our staff.</p></div>
  <div class="step" style="left:457px"><svg width="30" height="30" fill="none" stroke="#1e8ff0" stroke-width="2"><path d="M15 2l11 4v8c0 7-5 11-11 14C9 25 4 21 4 14V6z"/><path d="M10 15l4 4 6-8"/></svg><h4>GET FIXED</h4><p>Get fixed IMMEDIATELY! Our staff will solve your computer issues right before your eyes.</p></div>
  <div class="step" style="left:732px"><svg width="34" height="30" fill="none" stroke="#1e8ff0" stroke-width="2"><path d="M9 22a7 7 0 0 1 0-14 9 9 0 0 1 17 2 6 6 0 0 1 0 12"/><path d="M17 28V14M12 19l5-5 5 5"/></svg><h4>BACKUP YOUR INFORMATION!</h4><p>Saving your files is now EASY! You will be able to retain your personal files without any worry.</p></div>
  <a class="btn" href="#">View Our Services</a>
</section>

<section class="abs testi">
  <h2>TESTIMONIALS</h2>
  <div class="quote" style="left:256px"><div class="stars">★★★★★</div>I contacted them about a serious threat on my laptop, they have completely transformed the laptop. It now functions like a brand new laptop, the staff were excellent, really patient and helpful, excellent service and I would highly recommend, thank you.<div class="who">Daniel Marsh</div></div>
  <div class="quote" style="left:621px"><div class="stars">★★★★★</div>Offered a first class service. Answered all my problems very quickly. I had been having issues with my computer for a long time and the technicians helped me with lots of patience. Their service helped me fix the issues without me having to take the computer to a shop. Thank you<div class="who">Daniel Marsh</div></div>
  <div class="tdots"><span class="on"></span><span></span></div>
</section>

<section class="abs calltoday">
  <h2>CALL US TODAY</h2>
  <h3>And get started with our dedicated technicians.</h3>
  <div class="video" role="img" aria-label="Animated explainer video of a technician at a desk with a computer"><span class="play"></span></div>
  <p class="cap">Get a 30-minute one-on-one free consultation with one of our experts!</p>
</section>

<footer class="abs footer">
  <div class="logo"><i></i>brightdesk</div>
  <div class="f-about">
    <p>We are a group of technicians who work round the clock to ensure that your PC works perfectly. Get your computer free of suspicious software and have a healthy.</p>
    <p>You can get in touch with us any time of the day, any day of the week. We offer support through phone and online chat.</p>
  </div>
  <div class="f-h" style="left:522px;top:36px">Quick Links</div>
  <ul class="f-links"><li>About</li><li>Services</li><li>Benefits</li><li>Pricing</li><li>Contact</li><li>Premium Plan</li><li>Premium Plus Plan</li><li>Platinum Plan</li></ul>
  <div class="f-h" style="left:248px;top:214px">Trusted By</div>
  <div class="badges"><span style="width:44px;height:44px;border-radius:50%"></span><span style="width:40px;height:40px;border-radius:50%;background:#b9312d"></span><span style="width:52px;height:24px;background:#5a8a2e"></span></div>
  <div class="f-h" style="left:522px;top:214px">Follow Us</div>
  <div class="follow"><span></span><span></span><span></span><span></span></div>
  <div class="copy">Brightdesk © 2017. All rights reserved. Terms and Conditions · Refund Policy · Privacy Policy</div>
  <div class="contact-panel">
    <h3>Contact Us</h3>
    <div class="field">NAME</div>
    <div class="field">EMAIL</div>
    <div class="field msg">MESSAGE</div>
    <span class="send">Send</span>
  </div>
</footer>

</body>
</html>
```